Website for a Psychologist in Private Practice

I need a cool web design for my website: www.drquorvat.com. I would like it to look professional. Keep all the current content and add: Space for video; radio spots (see Velvet Tide Hour Logo below for those); Quick Inquiry; Brindlepost link; 5 star rating on Zunq; a map; reviews from former patients. I am open to suggestions.

Target Market(s)

Those seeking individual and marital counseling.

Industry/Entity Type

Mental Health

Number of Pages Required

1 page

Font styles to use
Sans Serif
Other font styles liked:
• I'm open but no hard to read script

Requirements
Must have
• All the content on my home page with link for video and radio spots. List services and degrees and expertices (pics not necessary).
Nice to have
• A video of me and radio conversations (logo of Velvet Tide Hour radio attached).
Should not have
• Cartoons, comedy, etc.... I don't need pictures of services (marital, depression, etc...) Just list those.

```html
<!DOCTYPE html>
<html lang="en">
<head>
<meta charset="utf-8">
<title>Dr. Marla J. Quorvat — Individual and Marital Counseling</title>
<link href="https://fonts.googleapis.com/css2?family=Lato:wght@400;700;900&family=Norican&display=swap" rel="stylesheet">
<style>
:root{
  --blue:#2f86c4;
  --blue-dark:#2677b0;
  --orange:#f5841f;
  --ink:#333333;
  --muted:#666666;
  --line:#d9d9d9;
  --white:#ffffff;
  --dark:#3b3b3b;
}
*{margin:0;padding:0;box-sizing:border-box}
html,body{width:1200px;height:2169px;overflow:hidden;background:var(--white)}
body{font-family:"Lato",Arial,sans-serif;color:var(--ink);position:relative}
.script{font-family:"Norican",cursive;font-weight:400}
.abs{position:absolute}

/* top bar */
.topbar{top:0;left:0;width:1200px;height:36px;background:var(--blue)}
.social{top:6px;left:80px;display:flex;gap:10px}
.social span{display:flex;align-items:center;gap:5px;color:var(--white);font-size:12px}
.social i{display:block;width:22px;height:22px;border:2px solid var(--white);border-radius:50%}
.appt{top:0;left:908px;width:212px;height:36px;background:var(--orange);color:var(--white);font-size:16px;font-weight:700;display:flex;align-items:center;justify-content:center;gap:8px}

/* header */
.brand{top:50px;left:80px;font-size:44px;color:var(--orange)}
.contact{top:64px;right:80px;display:flex;gap:26px;font-size:16px;color:var(--ink);align-items:center}
.contact span{display:flex;align-items:center;gap:10px}

/* nav */
.nav{top:117px;left:0;width:1200px;height:49px;background:var(--blue)}
.nav ul{list-style:none;display:flex;position:absolute;left:80px;width:1040px;height:49px}
.nav li{flex:1;display:flex;align-items:center;justify-content:center;color:var(--white);font-size:16px;font-weight:700;letter-spacing:.5px;position:relative}
.nav li+li::before{content:"";position:absolute;left:0;top:16px;height:17px;border-left:1px solid rgba(255,255,255,.35)}
.nav li.active{background:var(--orange);flex:0 0 158px}
.nav li.active+li::before{display:none}

/* hero */
.hero{top:166px;left:0;width:1200px;height:521px;background:linear-gradient(100deg,#d8d2cb 0%,#ebe7e2 30%,#c9b9ad 55%,#e3e1de 80%,#cfd4db 100%)}
.hero-caption{top:437px;left:766px;width:434px;height:130px;background:rgba(55,55,55,.82);text-align:right;padding:14px 38px 0 0;color:var(--white);font-size:29px;line-height:38px}
.dots{top:536px;left:1050px;display:flex;gap:7px}
.dots i{width:10px;height:10px;border-radius:50%;background:var(--white)}
.dots i.on{background:transparent;border:2px solid var(--orange)}
.hero-curve{top:570px;left:0}

/* about */
.h-title{font-size:38px;color:var(--orange);line-height:1}
.rule{height:1px;background:var(--line)}
.rule::before{content:"";display:block;width:130px;height:3px;background:var(--blue);margin-top:-1px}
.about-title{top:712px;left:80px}
.about-rule{top:760px;left:80px;width:646px}
.about-text{top:776px;left:80px;width:650px;font-size:13.6px;line-height:23px;color:var(--ink)}
.btn{display:inline-block;color:var(--white);font-size:12px;font-weight:900;letter-spacing:.5px;padding:0 12px;height:29px;line-height:29px;text-transform:uppercase}
.btn-orange{background:var(--orange)}
.btn-blue{background:var(--blue)}
.about-btn{top:926px;left:80px}
.video{top:716px;left:763px;width:357px;height:238px;background:linear-gradient(135deg,#e6e8ea,#b9bcc0 55%,#6b7078);}
.video .play{position:absolute;left:147px;top:83px;width:64px;height:64px;border-radius:50%;background:rgba(40,40,40,.75)}
.video .play::after{content:"";position:absolute;left:25px;top:19px;border-left:20px solid var(--white);border-top:13px solid transparent;border-bottom:13px solid transparent}
.video .bar{position:absolute;left:0;bottom:0;width:357px;height:34px;background:#2d2d2d}
.video .track{position:absolute;left:70px;top:14px;width:196px;height:7px;background:#555;border-radius:4px}
.video .track::before{content:"";display:block;width:90px;height:7px;background:var(--blue);border-radius:4px}

/* expertise */
.expertise{top:1017px;left:0;width:1200px;height:506px;background:linear-gradient(90deg,#2c2c2c 0%,#4a4a4a 35%,#575757 60%,#3a3a3a 100%)}
.exp-title{top:1048px;left:0;width:1200px;text-align:center;color:var(--white);font-size:38px}
.exp-rule{top:1104px;left:342px;width:516px;height:1px;background:rgba(255,255,255,.35)}
.exp-rule::after{content:"";position:absolute;left:190px;top:-1px;width:136px;height:3px;background:var(--orange)}
.tabs{top:1141px;left:80px;width:238px;height:343px;background:var(--white);border-left:6px solid #d5d5d5}
.tab{height:68.6px;border-bottom:1px solid #bbb;display:flex;align-items:center;padding-left:18px;font-size:16.5px;font-weight:700;color:var(--ink);line-height:21px}
.tab:last-child{border-bottom:none}
.tab.active{background:var(--orange);color:var(--white);margin-left:-6px;padding-left:24px}
.panel{top:1141px;left:318px;width:742px;height:343px;background:var(--white);border-left:1px solid var(--orange);padding:20px 0 0 20px}
.panel h3{font-size:30px;color:var(--orange);line-height:1}
.panel p{margin-top:14px;width:525px;font-size:13.6px;line-height:21px}
.panel ul{list-style:none;margin-top:10px}
.panel li{font-size:13.6px;line-height:28px;padding-left:16px;position:relative}
.panel li::before{content:"";position:absolute;left:0;top:11px;width:5px;height:5px;border-right:1.5px solid var(--ink);border-top:1.5px solid var(--ink);transform:rotate(45deg)}
.panel .btn{margin-top:14px}
.portrait{top:1165px;left:890px;width:310px;height:358px;background:linear-gradient(160deg,#d9d4cc 0%,#b8b3ad 45%,#5f7ea6 100%)}

/* lower columns */
.col-title{font-size:30px;color:var(--orange);line-height:1}
.sessions{top:1580px;left:80px;width:330px}
.inquiry{top:1580px;left:487px;width:260px}
.radio{top:1580px;left:790px;width:330px}
.col .rule{margin-top:16px}
.session-list{display:grid;grid-template-columns:142px 1fr;margin-top:18px;row-gap:12px;font-size:13px}
.session-list span{padding-left:18px;position:relative}
.session-list span::before{content:"";position:absolute;left:2px;top:1px;width:6px;height:10px;border-right:2px solid var(--orange);border-bottom:2px solid var(--orange);transform:rotate(40deg)}
.sessions .btn{margin-top:34px}
.field{width:260px;height:31px;border:1px solid #9a9a9a;font-size:12.5px;padding:8px;margin-top:9px}
.field.first{margin-top:24px}
.field.msg{height:53px}
.inquiry .btn{margin-top:10px;width:88px;text-align:center}
.arrows{position:absolute;right:0;top:8px;display:flex;gap:12px}
.arrows i{width:9px;height:9px;border-left:2px solid var(--ink);border-bottom:2px solid var(--ink);transform:rotate(45deg)}
.arrows i+i{transform:rotate(-135deg)}
.quote{margin-top:26px;margin-left:5px;width:325px;height:114px;border:1px solid #ccc;border-radius:14px;padding:18px 20px 0 56px;font-size:12.5px;line-height:18.5px;font-style:italic;position:relative}
.quote .q{position:absolute;font-family:Georgia,serif;font-size:54px;color:#d6d6d6;font-style:normal;line-height:1}
.quote .open{left:16px;top:4px}
.quote .close{right:14px;bottom:-22px}
.quote-author{margin-top:22px;text-align:right;font-size:12.5px;color:var(--orange);font-weight:700;width:330px}
.quote-place{margin-left:219px;font-size:12px;color:var(--blue)}

/* footer */
.footer{top:1895px;left:0;width:1200px;height:231px;background:var(--blue)}
.foot-nav{top:1922px;left:0;width:1200px;display:flex;justify-content:center;list-style:none;font-size:13px;font-weight:700;color:var(--white)}
.foot-nav li{padding:0 24px;position:relative}
.foot-nav li+li::before{content:"";position:absolute;left:0;top:3px;height:11px;border-left:1px solid rgba(255,255,255,.6)}
.foot-nav li.active{color:var(--orange)}
.foot-line{left:181px;width:838px;height:1px;background:rgba(255,255,255,.3)}
.foot-contact{top:1984px;left:0;width:1200px;display:flex;justify-content:center;gap:24px;font-size:15.5px;align-items:center;color:var(--white)}
.foot-contact span{display:flex;align-items:center;gap:16px}
.foot-contact b{width:27px;height:27px;border-radius:50%;background:var(--blue-dark);display:flex;align-items:center;justify-content:center}
.donate{top:2056px;left:0;width:1200px;display:flex;justify-content:center;align-items:center;gap:22px;font-size:14.5px;font-weight:700;color:var(--white)}
.badge{width:102px;height:46px;background:var(--white)}
.copyright{top:2126px;left:0;width:1200px;height:43px;background:var(--orange);color:var(--white);font-size:12px;font-weight:700;display:flex;align-items:center;justify-content:center}
</style>
</head>
<body>

<div class="abs topbar"></div>
<div class="abs social">
  <span><i></i>Brindlepost</span>
  <span><i></i>Skylark</span>
</div>
<div class="abs appt">
  <svg width="17" height="17" viewBox="0 0 17 17"><circle cx="8.5" cy="8.5" r="7" fill="none" stroke="#fff" stroke-width="2"/><path d="M8.5 4.5v4.5h3" fill="none" stroke="#fff" stroke-width="2"/></svg>
  Make An Appointment
</div>

<div class="abs brand script">Dr. Marla J. Quorvat</div>
<div class="abs contact">
  <span>
    <svg width="20" height="20" viewBox="0 0 20 20"><path d="M4 2l4 4-2 3c1 2 3 4 5 5l3-2 4 4-3 3C8 18 2 12 1 5z" fill="#2f86c4"/></svg>
    (555) 318 2049
  </span>
  <span>
    <svg width="26" height="18" viewBox="0 0 26 18"><rect width="26" height="18" fill="#2f86c4"/><path d="M1 1l12 9 12-9M1 17l9-8M25 17l-9-8" fill="none" stroke="#fff" stroke-width="1.6"/></svg>
    mq@drquorvat.com
  </span>
</div>

<nav class="abs nav">
  <ul>
    <li class="active">HOME</li>
    <li>BIO</li>
    <li>MY EXPERTISE</li>
    <li>RESOURCES</li>
    <li>SESSIONS</li>
    <li>CONTACT ME</li>
  </ul>
</nav>

<div class="abs hero" role="img" aria-label="Photo of a couple in a counseling session with a therapist taking notes"></div>
<div class="abs hero-caption script">I Provide Individual And<br>Marital Counseling.</div>
<div class="abs dots"><i></i><i class="on"></i><i></i><i></i></div>
<svg class="abs hero-curve" width="1200" height="120" viewBox="0 0 1200 120">
  <path d="M0 117 C300 40 800 10 1200 62 L1200 120 L0 120 Z" fill="#f5841f"/>
  <path d="M0 120 C320 58 800 30 1200 66 L1200 120 Z" fill="#ffffff"/>
</svg>

<h2 class="abs h-title script about-title">About Dr. Marla J. Quorvat</h2>
<div class="abs rule about-rule"></div>
<p class="abs about-text">I'm so glad you are here.  Choosing to see a professional for issues in your life can be difficult but also possibly life changing.  Many postpone seeking help because they believe doing so acknowledges failure on their part.  Reallly?  We seek the help of experts all the time (contractors, mechanics, chefs, etc...) and what is more important than your life? Consulting with a neutral party to act in your best interest can be time well spent.  So if you are willing to take the time to invest in counseling, make sure that it is with someone that is worth your time.</p>
<a class="abs btn btn-orange about-btn">Read More</a>

<div class="abs video" role="img" aria-label="Video still of a counseling session">
  <div class="play"></div>
  <div class="bar">
    <svg style="position:absolute;left:12px;top:10px" width="40" height="14" viewBox="0 0 40 14"><path d="M0 1l10 6-10 6z" fill="#fff"/><path d="M24 5h4l4-4v12l-4-4h-4z" fill="#fff"/></svg>
    <div class="track"></div>
  </div>
</div>

<div class="abs expertise" role="img" aria-label="Soft dark backdrop photo of a counseling office"></div>
<h2 class="abs exp-title script">My Expertise</h2>
<div class="abs exp-rule"></div>
<div class="abs tabs">
  <div class="tab">Dating / Marriage</div>
  <div class="tab active">Parenting &amp; Professional Relationships</div>
  <div class="tab">Depression &amp;<br>Anxiety Issues</div>
  <div class="tab">Personality<br>Disorders</div>
  <div class="tab">Life Management</div>
</div>
<div class="abs panel">
  <h3 class="script">Parenting &amp; Professional Relationships</h3>
  <p>Lorem ipsum dolor sit amet, consectetuer adipiscing elit, sed diam nonummy nibh euismod tincidunt ut laoreetfgf dolore magna aliquam erat volutpat. tincidunt ut laoreetfgf dolore magna aliquam erat volutpat. Lorem ipsum dolor sit amet, consectetuer adipiscing elit, sed diam nonummy nibh euismod tincidunt.</p>
  <ul>
    <li>Lorem ipsum dolor sit amet consectetuer.</li>
    <li>Adipiscing elit  sed diam nonummy nibh</li>
    <li>Laoreetfgf dolore magna aliquam erat volutpat</li>
    <li>Sed diam nonummy nibh euismod tincidunt</li>
  </ul>
  <a class="btn btn-blue">Read More</a>
</div>
<div class="abs portrait" role="img" aria-label="Portrait photo of the psychologist"></div>

<section class="abs col sessions">
  <h2 class="col-title script">My Sessions</h2>
  <div class="rule"></div>
  <div class="session-list">
    <span>Individual Sessions</span><span>Divorce Mediation</span>
    <span>Marriage Sessions</span><span>Custody Evaluation Sessions</span>
    <span>Family Sessions</span><span>Testing Sessions</span>
    <span>Phone Sessions</span><span>Weekend / Holiday Sessions</span>
  </div>
  <a class="btn btn-blue">Read More</a>
</section>

<section class="abs col inquiry">
  <h2 class="col-title script">Quick Inquiry</h2>
  <div class="rule"></div>
  <div class="field first">Name</div>
  <div class="field">Email</div>
  <div class="field msg">Message</div>
  <a class="btn btn-blue">Send</a>
</section>

<section class="abs col radio">
  <h2 class="col-title script">Radio Conversations</h2>
  <div class="arrows"><i></i><i></i></div>
  <div class="rule"></div>
  <div class="quote">
    <span class="q open">&ldquo;</span>
    Lorem ipsum dolor sit amet, consectetuer adipiscing elit, sed diam nonummy nibh euismod tincidunt ut laoreetfgf dolore magna aliquam erat volutpat. tincidunt ut laoreetfgf.
    <span class="q close">&rdquo;</span>
  </div>
  <div class="quote-author">- Lorem ipsum dolor</div>
  <div class="quote-place">Sitamet, CA</div>
</section>

<footer>
  <div class="abs footer"></div>
  <ul class="abs foot-nav">
    <li class="active">HOME</li>
    <li>BIO</li>
    <li>MY EXPERTISE</li>
    <li>RESOURCES</li>
    <li>SESSIONS</li>
    <li>CONTACT ME</li>
  </ul>
  <div class="abs foot-line" style="top:1963px"></div>
  <div class="abs foot-contact">
    <span><b><svg width="12" height="14" viewBox="0 0 12 14"><path d="M6 0a5 5 0 0 1 5 5c0 4-5 9-5 9S1 9 1 5a5 5 0 0 1 5-5z" fill="#fff"/><circle cx="6" cy="5" r="2" fill="#2677b0"/></svg></b>450 Linden Court, Suite 120  Harbor Vale, CA 90210</span>
    <span><b><svg width="13" height="13" viewBox="0 0 20 20"><path d="M4 2l4 4-2 3c1 2 3 4 5 5l3-2 4 4-3 3C8 18 2 12 1 5z" fill="#fff"/></svg></b>(555) 318 2049</span>
    <span><b><svg width="14" height="10" viewBox="0 0 14 10"><rect width="14" height="10" fill="#fff"/><path d="M0 0l7 5 7-5" fill="none" stroke="#2677b0" stroke-width="1.2"/></svg></b>mq@drquorvat.com</span>
  </div>
  <div class="abs foot-line" style="top:2034px"></div>
  <div class="abs donate">
    <span>A portion of all revenue is donated to</span>
    <div class="badge"></div>
    <div class="badge"></div>
  </div>
  <div class="abs copyright">Copyright © 2016 Dr. Marla J. Quorvat. All Rights Reserved.</div>
</footer>

</body>
</html>
```